Animal Eye Clinic needs a Business card

We are a new veterinary ophthalmology practice (Silverbrook Pet Vision Care) and we need a business card designed. We only see animal eyes - we are not a regular veterinary clinic. We already have a logo. We are looking for a professional, good looking business card to hand out to our clients. We are looking for something simple but professional and contemporary. Our logo is likely the only picture/graphic that needs to be on the card.

Contact Information for Business Card

Marisol Quent, BSc, DVM, MSc, DipACVO
Veterinary Ophthalmologist

Phone: 250.419.3067
Email: silverbrookpetvisioncare@mailvero.com
Website: silverbrookpetvisioncare.com
Address: 1875 Tessock Rd
Kelowna, BC, V4T 8M3

Colors

Designer to choose colors to be used in the design.

Requirements
Must have
• Our logo (attached)

```html
<!DOCTYPE html>
<html lang="en">
<head>
<meta charset="utf-8">
<title>Silverbrook Pet Vision Care – Business Card</title>
<link rel="stylesheet" href="https://fonts.googleapis.com/css2?family=Open+Sans:wght@400;600;700&display=swap">
<style>
  :root {
    --teal: #0a97a8;
    --ink: #1d1f21;
    --text-grey: #5a5a5a;
    --soft-grey: #8a8a8a;
    --paper: #ffffff;
    --backdrop: #d9d9d9;
  }
  * { box-sizing: border-box; margin: 0; padding: 0; }
  html, body {
    width: 1200px; height: 800px; overflow: hidden;
    background: var(--backdrop);
    font-family: "Open Sans", Arial, sans-serif;
  }
  .canvas {
    position: relative; width: 1200px; height: 800px;
  }
  .card {
    position: absolute; left: 320px; width: 560px; height: 320px;
    overflow: hidden;
    box-shadow: 0 6px 18px rgba(0,0,0,0.18);
  }
  .card--front { top: 50px; background: var(--paper); }
  .card--back { top: 430px; background: var(--ink); }

  .front-band {
    position: absolute; left: 0; right: 0; bottom: 0; height: 12px;
    background: var(--teal);
  }
  .brand {
    position: absolute; display: flex; align-items: center; gap: 12px;
    color: var(--teal); font-weight: 700;
  }
  .brand__dot {
    flex: none; border-radius: 50%; background: var(--teal);
  }
  .card--front .brand { top: 58px; right: 40px; font-size: 22px; }
  .card--front .brand__dot { width: 34px; height: 34px; }

  .contact {
    position: absolute; left: 40px; bottom: 42px;
    color: var(--text-grey); font-size: 13.5px; line-height: 1.55;
  }
  .contact__name { color: var(--teal); font-weight: 700; font-size: 17px; }
  .contact__creds { color: var(--teal); font-weight: 400; font-size: 12px; }
  .contact__row { display: flex; align-items: center; gap: 8px; }
  .contact__icon { width: 12px; height: 12px; flex: none; }

  .card--back .brand {
    top: 110px; left: 0; right: 0; justify-content: center;
    font-size: 26px;
  }
  .card--back .brand__dot { width: 46px; height: 46px; }
  .back-web {
    position: absolute; top: 172px; left: 0; right: 0; text-align: center;
    color: var(--soft-grey); font-size: 14px; letter-spacing: 2px;
  }
</style>
</head>
<body>
<main class="canvas">
  <section class="card card--front" aria-label="Card front">
    <div class="brand">
      <span class="brand__dot"></span>
      <span class="brand__name">Silverbrook Pet Vision Care</span>
    </div>
    <div class="contact">
      <p class="contact__name">Marisol Quent, <span class="contact__creds">BSc, DVM, MSc, DipACVO</span></p>
      <p>Veterinary Ophthalmologist</p>
      <p>1875 Tessock Rd Kelowna, BC, V4T 8M3</p>
      <p class="contact__row">
        <svg class="contact__icon" viewBox="0 0 12 12"><path d="M2.5 1h2l1 2.5-1.3 1a6 6 0 0 0 3.3 3.3l1-1.3 2.5 1v2c0 .8-.7 1.5-1.5 1.5A9 9 0 0 1 1 2.5C1 1.7 1.7 1 2.5 1z" fill="var(--teal)"/></svg>
        250.419.3067
      </p>
      <p class="contact__row">
        <svg class="contact__icon" viewBox="0 0 12 12"><rect x="0.5" y="2" width="11" height="8" rx="1" fill="var(--teal)"/><path d="M1 2.8 6 6.5 11 2.8" stroke="#fff" stroke-width="1" fill="none"/></svg>
        silverbrookpetvisioncare@mailvero.com
      </p>
      <p class="contact__row">
        <svg class="contact__icon" viewBox="0 0 12 12"><circle cx="6" cy="6" r="5.5" fill="var(--teal)"/><path d="M.5 6h11M6 .5c-2.5 3-2.5 8 0 11M6 .5c2.5 3 2.5 8 0 11" stroke="#fff" stroke-width=".8" fill="none"/></svg>
        silverbrookpetvisioncare.com
      </p>
    </div>
    <div class="front-band"></div>
  </section>

  <section class="card card--back" aria-label="Card back">
    <div class="brand">
      <span class="brand__dot"></span>
      <span class="brand__name">Silverbrook Pet Vision Care</span>
    </div>
    <p class="back-web">www.silverbrookpetvisioncare.com</p>
  </section>
</main>
</body>
</html>
```